Front page of Orthodox Christian Monastery Website

I am attaching a couple of versions of design that was already created for the front page of the website. You can grab the same pictures and titles (do not need to know the Russian language) to create your own version of design.
Background: Monastery website contains sermons, stories about monastery life, monastery music of the sisterhood.
Main principles of the design:
1. Various materials/sermons/music have to be clearly visible immediately to the site visitor.
2. Text descriptions to photos should be using font with a good contrast, highly clickable and easily readable.
3. Every article should have a photo or a quality picture (use those in the sample) that will convey something about it.
4. On the top, there will be a menu, which will be a line of words (just use generic words for now).
5. Design should reflect Christian Orthodox themes and fonts.
Updates

Target Market(s)

Orthodox Christian believers around the world and those that are interested in Orthodox Christianity

Number of Pages Required

1 page

Font styles to use
Serif

Colors

Designer to choose colors to be used in the design.

Requirements
Must have
• In the project description
Nice to have
• for some ideas see a popular Orthodox Christian website:
• www.blagovestnik-sample.ru
• We don't want to copy it, but it could give ideas.
Should not have
• Should not be overly complex

```html
<!DOCTYPE html>
<html lang="en">
<head>
<meta charset="utf-8">
<title>Orthodox Christian Monastery</title>
<link rel="stylesheet" href="https://fonts.googleapis.com/css2?family=Old+Standard+TT:wght@400;700&family=Montserrat:wght@400;500;600&family=Open+Sans:wght@400;600&display=swap">
<style>
:root{
  --green:#1d6b1f;
  --green-deep:#12561a;
  --green-dark:#0c3d10;
  --red:#8c1c1f;
  --red-soft:#93343a;
  --ink:#333;
  --muted:#666;
  --line:#d8d8d8;
  --white:#fff;
}
*{margin:0;padding:0;box-sizing:border-box}
html,body{width:1200px;height:2571px;overflow:hidden}
body{position:relative;background:var(--white);font-family:'Open Sans',sans-serif;color:var(--ink)}
.abs{position:absolute}
.sky{left:0;top:0;width:1200px;height:660px;background:linear-gradient(180deg,#5f9fd6 0%,#9ec7ea 40%,#d7e8f5 75%,#fff 100%)}
.brand{left:194px;top:30px;font-family:'Old Standard TT',serif;font-weight:700;font-size:28px;line-height:25px;color:var(--green);letter-spacing:1px}
.search{left:715px;top:45px;width:286px;height:32px;background:#f2f2f2;display:flex;align-items:center;padding-left:12px;gap:8px;font-family:'Montserrat',sans-serif;font-size:9px;color:#999;letter-spacing:.5px}
.nav{left:192px;top:103px;width:816px;height:46px;background:var(--green);display:flex;font-family:'Montserrat',sans-serif;font-size:13px;color:var(--white)}
.nav a{display:flex;align-items:center;padding:0 24px;color:inherit;text-decoration:none}
.nav a.active{background:var(--red);width:122px;justify-content:center}
.hero-main{left:192px;top:149px;width:523px;height:360px;background:linear-gradient(135deg,#5e4b3a,#3d4f7a 45%,#8a5a3a 75%,#c9a070)}
.hero-side{left:715px;width:293px;height:180px}
.hero-side.one{top:149px;background:radial-gradient(circle at 40% 40%,#f0b26a,#a0402a 55%,#3a1a18)}
.hero-side.two{top:329px;background:linear-gradient(160deg,#3b2a6a,#a13030 50%,#2a4a8a)}
.caption{font-family:'Montserrat',sans-serif;color:var(--white);text-shadow:0 1px 3px rgba(0,0,0,.5)}
.caption .t{font-size:17px;font-weight:500;letter-spacing:.5px}
.caption .s{font-size:12px;margin-top:5px}
.caption.small .t{font-size:14px}
.caption.small .s{font-size:10px;margin-top:2px}
.dots{left:666px;top:472px;display:flex;gap:5px}
.dots span{width:17px;height:17px;border-radius:50%;background:var(--white);display:flex;align-items:center;justify-content:center}
.sec-title{font-family:'Old Standard TT',serif;font-size:28px;color:#111;letter-spacing:.5px}
.rule{width:64px;height:4px;border-top:1px solid #777;border-bottom:1px solid #777}
.card{background:var(--white);border:1px solid var(--line);box-shadow:0 1px 3px rgba(0,0,0,.08)}
.card .ph{width:100%}
.card .body{padding:0 22px}
.card h3{font-family:'Montserrat',sans-serif;font-weight:500;color:var(--green);font-size:15px;margin:14px 0 6px}
.card p{font-size:10px;line-height:14px;color:var(--muted)}
.more{font-family:'Montserrat',sans-serif;font-weight:600;font-size:10px;color:var(--red);margin-top:10px;display:block}
.story .body{padding:0 20px}
.story h3{font-size:13px;color:#1a1a1a;margin:12px 0 4px;font-weight:600}
.story p{font-size:9px;line-height:12px}
.band{left:0;top:880px}
.stories-title{left:197px;top:986px;color:var(--white)}
.music-title{left:192px;top:1484px;line-height:32px}
.track{left:192px;width:533px;display:flex;gap:18px}
.track .ph{width:197px;height:132px;flex:none}
.track h3{font-family:'Montserrat',sans-serif;font-weight:500;color:var(--green);font-size:15px;margin:0 0 10px}
.track p{font-size:11.5px;line-height:17px;color:#444}
.track .more{font-size:11px;font-weight:500;margin-top:12px}
.sep{left:192px;width:533px;height:1px;background:var(--line)}
.life{left:759px;top:1490px;width:251px;height:821px;border:1px solid var(--line);background:var(--white)}
.life-head{height:48px;background:var(--red-soft);color:var(--white);font-family:'Old Standard TT',serif;font-size:21px;padding:12px 26px;letter-spacing:1px}
.post{position:absolute;left:20px;width:207px}
.post .ph{height:89px}
.post h4{font-family:'Montserrat',sans-serif;font-weight:500;color:var(--green);font-size:12px;margin:9px 0 5px}
.post p{font-size:9.5px;line-height:12px;color:#555}
.post .more{font-weight:500;margin-top:5px;font-size:9.5px}
.footer{left:0;top:2310px}
.foot-nav{left:0;top:2430px;width:1200px;display:flex;justify-content:center;gap:34px;font-family:'Montserrat',sans-serif;font-size:13px;color:var(--white)}
.copy{left:0;top:2461px;width:1200px;text-align:center;font-size:10px;color:#c9d8c9}
.social{left:528px;top:2494px;display:flex;gap:8px}
.social span{width:30px;height:30px;border:1.5px solid var(--white);border-radius:50%}
</style>
</head>
<body>
<div class="abs sky"></div>

<div class="abs brand">ORTHODOX CHRISTIAN<br>MONASTERY</div>
<div class="abs search">
  <svg width="13" height="13" viewBox="0 0 13 13"><circle cx="5.2" cy="5.2" r="4" fill="none" stroke="#777" stroke-width="1.8"/><line x1="8.2" y1="8.2" x2="12" y2="12" stroke="#777" stroke-width="2"/></svg>
  ENTER KEYWORD
</div>

<nav class="abs nav">
  <a class="active">HOME</a><a>ABOUT US</a><a>OUR BLOGS</a><a>ARTICLES</a><a>SERMONS</a><a>LIFE</a><a>CONTACT</a>
</nav>

<div class="abs hero-main" role="img" aria-label="Icon painting of saints gathered around the Holy Family"></div>
<div class="abs hero-side one" role="img" aria-label="Warm glowing church interior with a cross"></div>
<div class="abs hero-side two" role="img" aria-label="Stained glass window with a saint"></div>
<div class="abs caption" style="left:221px;top:442px"><div class="t">MORBI DIAM MAURIS VIVERRA IN GRAVIDA</div><div class="s">EU MATTIS IN ANTE MORBI EGET ARCU</div></div>
<div class="abs caption small" style="left:737px;top:282px"><div class="t">MAECENAS AT JUSTO ID VELIT</div><div class="s">DONEC DICTUM LECTUS</div></div>
<div class="abs caption small" style="left:737px;top:456px"><div class="t">CURABITUR IACULIS TEMPUS</div><div class="s">CURABITUR VEL MI SIT AMET</div></div>
<div class="abs dots">
  <span><svg width="8" height="8" viewBox="0 0 8 8"><path d="M5.5 1 2.5 4l3 3" fill="none" stroke="#333" stroke-width="1.5"/></svg></span>
  <span><svg width="8" height="8" viewBox="0 0 8 8"><path d="M2.5 1l3 3-3 3" fill="none" stroke="#333" stroke-width="1.5"/></svg></span>
</div>

<div class="abs sec-title" style="left:0;top:548px;width:1200px;text-align:center">SERMONS</div>
<div class="abs rule" style="left:566px;top:587px"></div>

<div class="abs card" style="left:192px;top:605px;width:262px;height:276px">
  <div class="ph" style="height:170px;background:linear-gradient(135deg,#6b4a30,#a0703f 50%,#5a3a22)" role="img" aria-label="Wooden letterpress blocks spelling sermon"></div>
  <div class="body"><h3>ARTICLE TITLE HERE</h3><p>Proin nulla arcu nonummy luctus dictum eget fermentum et lorema</p><span class="more">READ MORE ›</span></div>
</div>
<div class="abs card" style="left:468px;top:605px;width:264px;height:276px">
  <div class="ph" style="height:170px;background:radial-gradient(circle at 55% 65%,#f7e0b0,#b88a5a 45%,#4a3a30)" role="img" aria-label="Hands holding an open glowing book"></div>
  <div class="body"><h3>ARTICLE TITLE HERE</h3><p>Proin nulla arcu nonummy luctus dictum eget fermentum et lorema</p><span class="more">READ MORE ›</span></div>
</div>
<div class="abs card" style="left:746px;top:605px;width:264px;height:276px">
  <div class="ph" style="height:170px;background:linear-gradient(180deg,#8fa4b8,#b3a58a 50%,#8a6a40)" role="img" aria-label="Bronze sculpture of the Last Supper outdoors"></div>
  <div class="body"><h3>ARTICLE TITLE HERE</h3><p>Proin nulla arcu nonummy luctus dictum eget fermentum et lorema</p><span class="more">READ MORE ›</span></div>
</div>

<svg class="abs band" width="1200" height="570" viewBox="0 880 1200 570">
  <polygon points="880,965 1200,900 1200,995" fill="#c97a7e"/>
  <polygon points="960,965 1200,930 1200,995" fill="var(--red)"/>
  <polygon points="0,1335 270,1380 0,1395" fill="var(--red)"/>
  <polygon points="0,891 1200,960 1200,1440 0,1345" fill="var(--green-deep)"/>
</svg>

<div class="abs sec-title stories-title">STORIES ABOUT MONASTERY</div>
<div class="abs rule" style="left:199px;top:1024px;border-color:#cfe0cf"></div>

<div class="abs card story" style="left:195px;top:1054px;width:192px;height:243px">
  <div class="ph" style="height:132px;background:linear-gradient(180deg,#d9c7a0,#9a7040 60%,#6a4a2a)" role="img" aria-label="Ornate monastery library hall"></div>
  <div class="body"><h3>STORY TITLE</h3><p>Class aptent taciti sociosqu ad litora torquent per conubia nostra per inceptos hymenaeos Proin</p><span class="more">READ MORE ›</span></div>
</div>
<div class="abs card story" style="left:401px;top:1054px;width:192px;height:243px">
  <div class="ph" style="height:132px;background:linear-gradient(135deg,#5a2a1a,#b07040 50%,#3a2018)" role="img" aria-label="Carved wooden prayer wheels"></div>
  <div class="body"><h3>STORY TITLE</h3><p>Class aptent taciti sociosqu ad litora torquent per conubia nostra per inceptos hymenaeos Proin</p><span class="more">READ MORE ›</span></div>
</div>
<div class="abs card story" style="left:607px;top:1054px;width:192px;height:243px">
  <div class="ph" style="height:132px;background:radial-gradient(circle at 50% 70%,#e0a870,#a05a30 50%,#4a2414)" role="img" aria-label="Arched stone cloister corridor"></div>
  <div class="body"><h3>STORY TITLE</h3><p>Class aptent taciti sociosqu ad litora torquent per conubia nostra per inceptos hymenaeos Proin</p><span class="more">READ MORE ›</span></div>
</div>
<div class="abs card story" style="left:813px;top:1054px;width:192px;height:243px">
  <div class="ph" style="height:132px;background:linear-gradient(135deg,#2a5a8a,#b05a3a 50%,#3a7a5a)" role="img" aria-label="Colourful painted monastery fresco"></div>
  <div class="body"><h3>STORY TITLE</h3><p>Class aptent taciti sociosqu ad litora torquent per conubia nostra per inceptos hymenaeos Proin</p><span class="more">READ MORE ›</span></div>
</div>

<div class="abs sec-title music-title">MONASTERY MUSIC OF<br>THE SISTERHOOD</div>
<div class="abs rule" style="left:194px;top:1556px"></div>

<div class="abs track" style="top:1584px">
  <div class="ph" style="background:linear-gradient(135deg,#8a4a3a,#c08a6a 50%,#5a6a5a)" role="img" aria-label="Fresco of angels playing instruments"></div>
  <div><h3>Integer congue augue et malesuada</h3><p>Mauris vel lacus vitae felis vestibulum volutpat Etiam est nunc venenatis in tristique eu imperdiet ac nisl Cum sociis natoque penatibus et magnis dis parturient montes nascetur ridiculus mus In iaculis facilisis massa Etiam eu</p><span class="more">READ MORE</span></div>
</div>
<div class="abs sep" style="top:1741px"></div>
<div class="abs track" style="top:1771px">
  <div class="ph" style="background:linear-gradient(135deg,#1f4a9a,#b03030 45%,#d0a030 75%,#2a3a7a)" role="img" aria-label="Stained glass of saints with instruments"></div>
  <div><h3>Donec dictum lectus non odio</h3><p>Mauris vel lacus vitae felis vestibulum volutpat Etiam est nunc venenatis in tristique eu imperdiet ac nisl Cum sociis natoque penatibus et magnis dis parturient montes nascetur ridiculus mus In iaculis facilisis massa Etiam eu</p><span class="more">READ MORE</span></div>
</div>
<div class="abs sep" style="top:1930px"></div>
<div class="abs track" style="top:1965px">
  <div class="ph" style="background:linear-gradient(135deg,#e0b890,#c07a6a 50%,#7a8ab0)" role="img" aria-label="Painting of an angel playing a harp"></div>
  <div><h3>Pellentesque faucibus Ut accum</h3><p>Mauris vel lacus vitae felis vestibulum volutpat Etiam est nunc venenatis in tristique eu imperdiet ac nisl Cum sociis natoque penatibus et magnis dis parturient montes nascetur ridiculus mus In iaculis facilisis massa Etiam eu</p><span class="more">READ MORE</span></div>
</div>
<div class="abs sep" style="top:2125px"></div>
<div class="abs track" style="top:2157px">
  <div class="ph" style="background:linear-gradient(180deg,#3a2a22,#8a5a40 55%,#2a1a14)" role="img" aria-label="Sisterhood choir singing"></div>
  <div><h3>Aenean porttitor eros vel dolor Donec</h3><p>Mauris vel lacus vitae felis vestibulum volutpat Etiam est nunc venenatis in tristique eu imperdiet ac nisl Cum sociis natoque penatibus et magnis dis parturient montes nascetur ridiculus mus In iaculis facilisis massa Etiam eu</p><span class="more">READ MORE</span></div>
</div>

<aside class="abs life">
  <div class="life-head">LIFE</div>
  <div class="post" style="top:69px"><div class="ph" style="background:linear-gradient(135deg,#1a1a1a,#5a4a3a 60%,#2a2a2a)" role="img" aria-label="Hands clasped in prayer in low light"></div><h4>Blog Title here</h4><p>Class aptent taciti sociosqu ad litora torquent per conubia nostra per</p><span class="more">READ MORE</span></div>
  <div class="post" style="top:256px"><div class="ph" style="background:linear-gradient(135deg,#c08a40,#f0e0c0 50%,#6a4a2a)" role="img" aria-label="Open book in warm light"></div><h4>Blog Title here</h4><p>Class aptent taciti sociosqu ad litora torquent per conubia nostra per</p><span class="more">READ MORE</span></div>
  <div class="post" style="top:441px"><div class="ph" style="background:linear-gradient(90deg,#4a3020,#c0905a 55%,#f0e0c0)" role="img" aria-label="Woman praying quietly"></div><h4>Blog Title here</h4><p>Class aptent taciti sociosqu ad litora torquent per conubia nostra per</p><span class="more">READ MORE</span></div>
  <div class="post" style="top:626px"><div class="ph" style="background:radial-gradient(circle at 35% 50%,#f8e8b0,#8a7060 40%,#2a2a30)" role="img" aria-label="Lit candle in darkness"></div><h4>Blog Title here</h4><p>Class aptent taciti sociosqu ad litora torquent per conubia nostra per</p><span class="more">READ MORE</span></div>
</aside>

<svg class="abs footer" width="1200" height="261" viewBox="0 2310 1200 261">
  <path d="M0 2318 Q600 2420 1200 2318 L1200 2571 L0 2571 Z" fill="var(--green-dark)"/>
</svg>
<div class="abs foot-nav"><span>HOME</span><span>ABOUT US</span><span>OUR BLOGS</span><span>ARTICLES</span><span>SERMONS</span><span>LIFE</span><span>CONTACT</span></div>
<div class="abs copy">© 2018 Company Name &nbsp;All right reserved</div>
<div class="abs social"><span></span><span></span><span></span><span></span></div>
</body>
</html>
```